International Trading Company, 'KIRO' needs a Business Card

The company name is "KIRO" and it has own logo design.
I'd like to use its logo on this business card.
I need two side Business Card.
I'll look forward to your great design.
Thank you very much in advance.

Contact Information for Business Card

Company Name : Kiro Harbour Limited
Information Example
Dorian Pallister
Mobile(use icon please) : 1 (212) 555-0143
Tel(use icon please) : 1 (212) 555-0178
Email(use icon please) : dorian27@kiroharbour-mail.com
Address(use icon please) : 482 Halden Ave, New York, NY 10160, USA

```html
<!DOCTYPE html>
<html lang="en">
<head>
<meta charset="utf-8">
<title>Kiro Harbour Limited – Business Card</title>
<link rel="stylesheet" href="https://fonts.googleapis.com/css2?family=Arimo:wght@400;700&display=swap">
<style>
  :root {
    --card-bg: #111111;
    --brand-block: #060606;
    --brand-mark: #6f6f6f;
    --text-white: #ffffff;
    --rule-grey: #bdbdbd;
    --accent-bar: #b5b5b5;
  }
  * { margin: 0; padding: 0; box-sizing: border-box; }
  html, body {
    width: 1200px;
    height: 719px;
    overflow: hidden;
    background: var(--card-bg);
  }
  .card {
    position: relative;
    width: 1200px;
    height: 719px;
    background: var(--card-bg);
    font-family: "Arimo", Arial, sans-serif;
    color: var(--text-white);
  }
  .brand-block {
    position: absolute;
    left: 692px;
    top: 27px;
    width: 508px;
    height: 166px;
    background: var(--brand-block);
  }
  .brand-lockup {
    position: absolute;
    left: 30px;
    top: 20px;
    display: flex;
    align-items: center;
    gap: 22px;
  }
  .brand-square {
    width: 58px;
    height: 58px;
    background: var(--brand-mark);
  }
  .brand-name {
    font-size: 76px;
    font-weight: 700;
    line-height: 1;
    color: var(--text-white);
  }
  .brand-tagline {
    position: absolute;
    left: 29px;
    right: 18px;
    top: 114px;
    display: flex;
    justify-content: space-between;
    font-size: 31px;
    font-weight: 400;
    line-height: 1.2;
    color: var(--text-white);
  }
  .name-bar {
    position: absolute;
    left: 102px;
    top: 422px;
    width: 14px;
    height: 79px;
    background: var(--accent-bar);
  }
  .person-name {
    position: absolute;
    left: 147px;
    top: 438px;
    font-size: 35px;
    font-weight: 700;
    line-height: 1;
  }
  .divider {
    position: absolute;
    left: 107px;
    top: 523px;
    width: 1018px;
    height: 2px;
    background: var(--rule-grey);
  }
  .contact {
    position: absolute;
    display: flex;
    align-items: center;
    font-size: 25px;
    line-height: 1;
    white-space: nowrap;
  }
  .contact svg { fill: var(--text-white); flex: none; }
  .contact-mobile { left: 96px; top: 556px; gap: 16px; }
  .contact-tel { left: 406px; top: 560px; gap: 12px; }
  .contact-email { left: 716px; top: 556px; gap: 20px; font-size: 24px; }
  .contact-address { left: 90px; top: 628px; gap: 38px; }
</style>
</head>
<body>
<main class="card">
  <div class="brand-block">
    <div class="brand-lockup">
      <div class="brand-square"></div>
      <div class="brand-name">KIRO</div>
    </div>
    <div class="brand-tagline"><span>Kiro</span><span>Harbour</span><span>Limited</span></div>
  </div>

  <div class="name-bar"></div>
  <h1 class="person-name">Dorian Pallister</h1>
  <div class="divider"></div>

  <div class="contact contact-mobile">
    <svg width="24" height="40" viewBox="0 0 24 40" aria-hidden="true">
      <path d="M4 0h16a4 4 0 0 1 4 4v32a4 4 0 0 1-4 4H4a4 4 0 0 1-4-4V4a4 4 0 0 1 4-4zm0 6v25h16V6zm8 27a2.5 2.5 0 1 0 0 5a2.5 2.5 0 0 0 0-5z"/>
    </svg>
    <span>1 (212) 555-0143</span>
  </div>

  <div class="contact contact-tel">
    <svg width="36" height="30" viewBox="0 0 36 30" aria-hidden="true">
      <path d="M2 9c0-5 7-8 16-8s16 3 16 8v3h-8V8c-2-1-5-1.5-8-1.5S12 7 10 8v4H2z"/>
      <path d="M8 14h20l5 14H3zm10 3a4.5 4.5 0 1 0 0 9a4.5 4.5 0 0 0 0-9z"/>
    </svg>
    <span>1 (212) 555-0178</span>
  </div>

  <div class="contact contact-email">
    <svg width="34" height="34" viewBox="0 0 34 34" aria-hidden="true">
      <circle cx="17" cy="17" r="16"/>
      <text x="17" y="24" text-anchor="middle" font-family="Arimo, Arial, sans-serif" font-size="22" font-weight="700" fill="#111111">@</text>
    </svg>
    <span>dorian27@kiroharbour-mail.com</span>
  </div>

  <div class="contact contact-address">
    <svg width="50" height="42" viewBox="0 0 50 42" aria-hidden="true">
      <path d="M6 26h38l6 16H0z"/>
      <path d="M25 0a11 11 0 0 1 11 11c0 8-11 18-11 18S14 19 14 11A11 11 0 0 1 25 0zm0 6a5 5 0 1 0 0 10a5 5 0 0 0 0-10z"/>
    </svg>
    <span>482 Halden Ave, New York, NY 10160, USA</span>
  </div>
</main>
</body>
</html>
```